Telmoro Business Card

I already have the conplay logo. I need to develop a professional business card layout

Target Market(s)

Business

Industry/Entity Type

Business

Contact Information for Business Card

Company Name: Telmoro Limited

Font styles to use
Sans Serif

Colors

Designer to choose colors to be used in the design.

Requirements
Must have
• Use current logo
• Need two card size options:
• Small Card: 70mm x 28mm (Landscape)
• Square Card: 65mm x 65mm
Nice to have
• I will need 8-10 files for each name, number and email address (details to follow)

```html
<!DOCTYPE html>
<html lang="en">
<head>
<meta charset="utf-8">
<title>Telmoro Business Cards</title>
<link href="https://fonts.googleapis.com/css2?family=Oswald:wght@300;500;600;700&display=swap" rel="stylesheet">
<style>
  :root {
    --page: #ffffff;
    --card: #ffffff;
    --ink: #1c1c1c;
    --brand: #0a00c8;
    --swatch-forest: #127f00;
    --swatch-lime: #84ff00;
    --swatch-yellow: #fbe200;
    --swatch-red: #fd0008;
    --swatch-sky: #4dd3ff;
    --swatch-blue: #0000cc;
  }
  * { margin: 0; padding: 0; box-sizing: border-box; }
  html, body {
    width: 1200px; height: 1000px; overflow: hidden;
    background: var(--page);
    font-family: "Oswald", sans-serif;
    color: var(--ink);
  }
  .canvas { position: relative; width: 1200px; height: 1000px; }

  .card {
    position: absolute;
    background: var(--card);
    box-shadow: 0 6px 18px rgba(0,0,0,0.10);
  }
  .card--tall { left: 142px; top: 134px; width: 294px; height: 734px; }
  .card--square { left: 545px; top: 244px; width: 513px; height: 512px; }

  .swatch { position: absolute; }
  .swatch--forest { background: var(--swatch-forest); }
  .swatch--lime { background: var(--swatch-lime); }
  .swatch--yellow { background: var(--swatch-yellow); }
  .swatch--red { background: var(--swatch-red); }
  .swatch--sky { background: var(--swatch-sky); }
  .swatch--blue { background: var(--swatch-blue); }

  .swatch-row .swatch { top: 0; width: 40px; height: 30px; }
  .swatch-column .swatch { right: 0; width: 23px; height: 26px; }

  .details { position: absolute; line-height: 1; }
  .details--left { left: 54px; top: 96px; text-align: left; }
  .details--right { right: 57px; top: 277px; text-align: right; }

  .company { font-weight: 600; font-size: 20px; letter-spacing: 2.6px; }
  .person { font-weight: 600; font-size: 31px; letter-spacing: 2.8px; margin-top: 14px; }
  .address { font-weight: 300; font-size: 25px; letter-spacing: 1.4px; line-height: 31px; margin-top: 2px; }
  .phone { font-weight: 600; font-size: 21px; letter-spacing: 1.6px; margin-top: 18px; }
  .email { font-weight: 600; font-size: 20px; letter-spacing: 0.8px; margin-top: 10px; }

  .brand-name {
    position: absolute;
    transform-origin: left top;
    transform: rotate(-90deg);
    font-weight: 700;
    font-size: 62px;
    line-height: 47px;
    height: 47px;
    letter-spacing: 1px;
    color: var(--brand);
    white-space: nowrap;
  }
  .card--tall .brand-name { left: 53px; top: 684px; }
  .card--square .brand-name { left: 56px; top: 341px; }
</style>
</head>
<body>
<div class="canvas">

  <section class="card card--tall" aria-label="Small business card">
    <div class="swatch-row">
      <span class="swatch swatch--forest" style="left:0"></span>
      <span class="swatch swatch--lime" style="left:51px"></span>
      <span class="swatch swatch--yellow" style="left:102px"></span>
      <span class="swatch swatch--red" style="left:153px"></span>
      <span class="swatch swatch--sky" style="left:204px"></span>
      <span class="swatch swatch--blue" style="left:255px"></span>
    </div>
    <div class="details details--left">
      <p class="company">TELMORO LIMITED</p>
      <p class="person">ALEX MORGAN</p>
      <p class="address">33 Telmoro Street,<br>TELMORO 26321</p>
      <p class="phone">+61 400 555 012</p>
      <p class="email">alex@telmoro.com</p>
    </div>
    <p class="brand-name">TELMORO</p>
  </section>

  <section class="card card--square" aria-label="Square business card">
    <p class="brand-name">TELMORO</p>
    <div class="details details--right">
      <p class="company">TELMORO LIMITED</p>
      <p class="person">ALEX MORGAN</p>
      <p class="address">33 Telmoro Street,<br>TELMORO 26321</p>
      <p class="phone">+61 400 555 012</p>
      <p class="email">alex@telmoro.com</p>
    </div>
    <div class="swatch-column">
      <span class="swatch swatch--forest" style="top:279px"></span>
      <span class="swatch swatch--lime" style="top:313px"></span>
      <span class="swatch swatch--yellow" style="top:347px"></span>
      <span class="swatch swatch--red" style="top:381px"></span>
      <span class="swatch swatch--sky" style="top:415px"></span>
      <span class="swatch swatch--blue" style="top:449px"></span>
    </div>
  </section>

</div>
</body>
</html>
```